Salon website

Need a web design for a new blow dry and hair extension boutique in CT
would like the color scheme to be gray, white and tiffany blue
Create a web site with about 4 pages showing
1 about us page
1 blow dry services page
1 hair extension services page
1 contact us page
1 membership page
1 parties page

Industry/Entity Type

Boutique

Colors
86cfc6
cfeae6
33b7a4
aaaaaa
cbcbcb
ffffff

```html
<!DOCTYPE html>
<html lang="en">
<head>
<meta charset="utf-8">
<title>Hair Salon — Blow Dry and Hair Extension Boutique</title>
<link rel="stylesheet" href="https://fonts.googleapis.com/css2?family=Source+Sans+3:wght@300;400&display=swap">
<style>
  :root {
    --ink: #030405;
    --hair-deep: #0b1216;
    --hair-mid: #2c4350;
    --hair-light: #8fb3c4;
    --skin: #d9c4c4;
    --white: #ffffff;
    --nav-blue: #62d9e8;
    --divider: rgba(255, 255, 255, 0.9);
    --lavender: #efe4fb;
    --phone-box: rgba(20, 24, 28, 0.55);
  }
  * { margin: 0; padding: 0; box-sizing: border-box; }
  html, body {
    width: 1200px;
    height: 572px;
    overflow: hidden;
    background: var(--ink);
    font-family: "Source Sans 3", "Source Sans Pro", sans-serif;
  }
  .hero {
    position: relative;
    width: 1200px;
    height: 572px;
    overflow: hidden;
  }
  .hero-photo {
    position: absolute;
    inset: 0;
    background:
      radial-gradient(ellipse 180px 240px at 830px 330px, var(--skin) 0%, rgba(217,196,196,0.5) 45%, rgba(217,196,196,0) 100%),
      radial-gradient(ellipse 260px 200px at 1080px 120px, var(--hair-light) 0%, rgba(143,179,196,0) 100%),
      linear-gradient(100deg, var(--ink) 0%, var(--hair-deep) 22%, var(--hair-mid) 48%, #5d7c8c 62%, var(--hair-deep) 88%, var(--ink) 100%);
  }
  .main-nav {
    position: absolute;
    top: 114px;
    left: 294px;
    display: flex;
    height: 54px;
    border-left: 1px solid var(--divider);
  }
  .main-nav a {
    display: flex;
    align-items: center;
    justify-content: center;
    height: 100%;
    border-right: 1px solid var(--divider);
    color: var(--nav-blue);
    text-decoration: none;
    font-size: 20px;
    font-weight: 400;
    letter-spacing: 2px;
  }
  .nav-home, .nav-about, .nav-blowdry, .nav-contact { width: 128px; }
  .nav-extensions { width: 141px; }
  .brand-title {
    position: absolute;
    top: 236px;
    left: 0;
    width: 1200px;
    text-align: center;
    color: var(--white);
    font-size: 95px;
    font-weight: 300;
    line-height: 1;
    letter-spacing: 44px;
    padding-left: 44px;
  }
  .brand-tagline {
    position: absolute;
    top: 339px;
    left: 0;
    width: 1200px;
    text-align: center;
    font-size: 14px;
    font-weight: 400;
    letter-spacing: 16.7px;
    padding-left: 16.7px;
    line-height: 1;
  }
  .brand-tagline span {
    background: linear-gradient(90deg, #f3a0b8 0%, #f2d36a 22%, #9be3ff 45%, #f6b57a 62%, #c8b8f2 80%, #e8e8e8 100%);
    -webkit-background-clip: text;
    background-clip: text;
    color: transparent;
  }
  .contact-email {
    position: absolute;
    top: 432px;
    left: 0;
    width: 1200px;
    text-align: center;
    color: var(--lavender);
    font-size: 20px;
    font-weight: 300;
    letter-spacing: 7.5px;
    padding-left: 7.5px;
  }
  .contact-phone {
    position: absolute;
    top: 464px;
    left: 472px;
    width: 239px;
    height: 45px;
    display: flex;
    align-items: center;
    justify-content: center;
    background: var(--phone-box);
    color: var(--lavender);
    font-size: 27px;
    font-weight: 300;
    letter-spacing: 3px;
  }
</style>
</head>
<body>
  <header class="hero">
    <div class="hero-photo" role="img" aria-label="Photograph of a woman in profile with long, glossy black hair with blue highlights sweeping across the frame"></div>

    <nav class="main-nav">
      <a class="nav-home" href="#">Home</a>
      <a class="nav-about" href="#">About</a>
      <a class="nav-blowdry" href="#">Blow Dry</a>
      <a class="nav-extensions" href="#">Extenstions</a>
      <a class="nav-contact" href="#">Contact</a>
    </nav>

    <h1 class="brand-title">Hair Salon</h1>
    <p class="brand-tagline"><span>blow dry and hair extension boutique</span></p>

    <p class="contact-email">bookings@lumenhair.com</p>
    <p class="contact-phone">ph:555017246</p>
  </header>
</body>
</html>
```